Etiketten-Design für Himbeer-Gin
Zielgruppe
GIN
Aufgabenstellung
Wir benötigen ein Etikett für unseren neuen Himbeere GIN, der Name des GINs lautet: BrolettaGIN und soll für folgende Flasche dargestellt werden: https://www.flaschorix-beispiel.de/nolva-flasche-500ml-schwarz-beschichtet-kx17-karton-48stk.html
mit dem Etikett https://klebrano-beispiel.de/anwendungen/fluoreszierende-etiketten/ Himbeerlastiges Design mit bestehendem Logo (TorvaldGIN) siehe Daten. Bei Fragen stehe ich gerne zur Verfügung!

```html
<!DOCTYPE html>
<html lang="de">
<head>
<meta charset="utf-8">
<title>BrolettaGIN – Etikett</title>
<link rel="stylesheet" href="https://fonts.googleapis.com/css2?family=Oswald:wght@600&family=Space+Mono:wght@400;700&display=swap">
<style>
  :root {
    --label-bg: #231f1f;
    --raspberry: #f72a8a;
    --ink-light: #f4f1f1;
  }
  * { margin: 0; padding: 0; box-sizing: border-box; }
  html, body {
    width: 1200px;
    height: 800px;
    overflow: hidden;
    background: var(--label-bg);
  }
  .label {
    position: relative;
    width: 1200px;
    height: 800px;
    overflow: hidden;
    background: var(--label-bg);
    color: var(--ink-light);
    font-family: "Space Mono", monospace;
  }
  .side-panel {
    position: absolute;
    left: 34px;
    top: 748px;
    width: 670px;
    transform-origin: top left;
    transform: rotate(-90deg);
  }
  .brewery-name {
    font-weight: 700;
    font-size: 15px;
    line-height: 18px;
    letter-spacing: 5.6px;
    white-space: nowrap;
  }
  .brewery-name .dot {
    display: inline-block;
    width: 8px;
    height: 8px;
    border-radius: 50%;
    background: var(--ink-light);
    margin: 0 12px 2px 6px;
    vertical-align: middle;
  }
  .brewery-about {
    margin-top: 16px;
    font-size: 9.6px;
    line-height: 17.4px;
    letter-spacing: 1.45px;
  }
  .brewery-about span {
    display: block;
    white-space: nowrap;
  }
  .product-name {
    position: absolute;
    left: 0;
    width: 1200px;
    top: 118px;
    text-align: center;
    font-family: "Oswald", sans-serif;
    font-weight: 600;
    font-size: 187px;
    line-height: 1;
    letter-spacing: 1px;
    color: var(--raspberry);
    transform: scaleX(0.78);
    transform-origin: center top;
  }
  .fruit-art {
    position: absolute;
    left: 500px;
    top: 319px;
    width: 193px;
    height: 304px;
    border-radius: 48% 48% 46% 46% / 38% 38% 60% 60%;
    background: radial-gradient(ellipse at 50% 55%, rgba(247, 42, 138, 0.35), rgba(247, 42, 138, 0.08) 70%);
  }
  .strength {
    position: absolute;
    left: 0;
    width: 1192px;
    top: 652px;
    text-align: center;
    font-weight: 700;
    font-size: 30px;
    line-height: 38px;
    letter-spacing: 3.6px;
  }
  .origin {
    position: absolute;
    left: 0;
    width: 1192px;
    top: 705px;
    text-align: center;
    font-size: 10px;
    line-height: 16px;
    letter-spacing: 2.5px;
  }
  .base-stripe {
    position: absolute;
    left: 0;
    top: 768px;
    width: 1200px;
    height: 10px;
    background: var(--raspberry);
  }
</style>
</head>
<body>
  <main class="label">
    <aside class="side-panel">
      <p class="brewery-name">MUSTER BRAUEREI<span class="dot"></span>MUSTERSTADT</p>
      <p class="brewery-about">
        <span>Eine Craft-Brauerei ist eine Brauerei, die kleine Mengen an Bier herstellt, für gewöhnlich</span>
        <span>viel weniger als große Brauereiunternehmen; üblicherweise handelt es sich um unabhängige</span>
        <span>Unternehmen. Solche Brauereien zeichnen sich in der Regel durch ihren Fokus auf Qualität,</span>
        <span>Geschmack und Brautechnik aus.</span>
      </p>
    </aside>

    <h1 class="product-name">BrolettaGIN</h1>

    <div class="fruit-art" role="img" aria-label="Linienzeichnung einer Himbeere mit Blättern in Pink"></div>

    <p class="strength">18,5 % ALKOHOL</p>
    <p class="origin">GEBRAUT &amp; ABGEFÜLLT IN MUSTERSTADT</p>

    <div class="base-stripe"></div>
  </main>
</body>
</html>
```